kestrelnet9 - a safety solution for schools

A Amok App for schools needs your help to design some screens. Its important to have a very simple use of the app. The function of the app is very easy, you put the button to trigger the alarm. The app has a message function. So we need 3 howto screens. you find a better description of the project in the briefing-file. If you have any questions just ask. Thanks in advance for the suggestions. Best Regards, Lars

Target Market(s)

Schools

Industry/Entity Type

Security Service

Font styles to use
Sans Serif

Colors

Designer to choose colors to be used in the design.

Requirements
Must have
• Simple, easy to use, look like a security app, trust,

```html
<!DOCTYPE html>
<html lang="de">
<head>
<meta charset="utf-8">
<title>kestrelnet9 – Damit jede Sekunde zählt</title>
<link href="https://fonts.googleapis.com/css2?family=Poppins:wght@600&family=Roboto:wght@300;400;700;900&display=swap" rel="stylesheet">
<style>
  :root {
    --bg-dark: #1b0203;
    --photo-deep: #3a0a0c;
    --photo-mid: #5a1416;
    --photo-warm: #6e1a1a;
    --brand-cyan: #19e3d6;
    --accent-yellow: #f5c21b;
    --screen-red: #8a0c10;
    --alarm-glow: #ff5a5f;
    --screen-black: #0d0607;
  }
  * { margin: 0; padding: 0; box-sizing: border-box; }
  html, body { width: 1200px; height: 697px; overflow: hidden; background: var(--bg-dark); }
  .landing { position: relative; width: 1200px; height: 697px; background: var(--bg-dark); overflow: hidden; }

  .hero-photo {
    position: absolute; inset: 0;
    clip-path: polygon(0 0, 610px 0, 915px 697px, 0 697px);
    background:
      radial-gradient(ellipse 260px 340px at 390px 420px, rgba(40,8,12,.85), transparent 70%),
      linear-gradient(180deg, var(--photo-warm) 0%, var(--photo-mid) 45%, var(--photo-deep) 75%, #200506 100%);
  }

  .brand {
    position: absolute; left: 290px; top: 516px; width: 280px;
    text-align: center;
  }
  .brand__mark {
    width: 56px; height: 56px; margin: 0 auto 22px;
    border-radius: 50%; background: var(--accent-yellow);
  }
  .brand__name {
    font-family: "Poppins", sans-serif; font-weight: 600;
    font-size: 30px; line-height: 1; color: var(--brand-cyan);
  }
  .brand__tagline {
    margin-top: 16px;
    font-family: "Roboto", sans-serif; font-weight: 400;
    font-size: 14px; color: var(--accent-yellow);
  }

  .app-screen {
    position: absolute; left: 645px; top: 150px; width: 258px; height: 440px;
    overflow: hidden;
    background: linear-gradient(180deg, var(--screen-red) 0%, #4a0508 38%, var(--screen-black) 72%, var(--screen-black) 100%);
  }
  .app-screen__sheen {
    position: absolute; inset: 0;
    background: linear-gradient(180deg, rgba(255,255,255,.28), rgba(255,255,255,.08));
    clip-path: polygon(86px 0, 258px 0, 258px 362px);
  }
  .countdown { position: absolute; left: 49px; top: 78px; width: 160px; height: 160px; }
  .alert {
    position: absolute; left: 0; right: 0; top: 290px;
    text-align: center; font-family: "Roboto", sans-serif; color: var(--accent-yellow);
  }
  .alert__sender { font-weight: 300; font-size: 19px; line-height: 1.15; }
  .alert__message { font-weight: 900; font-size: 19px; line-height: 1.05; text-transform: uppercase; }
  .app-nav {
    position: absolute; left: 0; right: 0; top: 394px;
    display: flex; justify-content: center; gap: 48px;
  }
  .app-nav svg { width: 20px; height: 20px; }
</style>
</head>
<body>
<main class="landing">
  <div class="hero-photo" role="img" aria-label="Foto: Schülerin mit Rucksack auf dem Schulweg, in rotem Farbton"></div>

  <div class="brand">
    <div class="brand__mark"></div>
    <div class="brand__name">kestrelnet9</div>
    <div class="brand__tagline">Damit jede Sekunde zählt!</div>
  </div>

  <section class="app-screen" aria-label="Alarmbildschirm der App">
    <div class="app-screen__sheen"></div>

    <svg class="countdown" viewBox="0 0 160 160" aria-label="Countdown 4 Sekunden">
      <defs>
        <radialGradient id="core" cx="50%" cy="45%" r="55%">
          <stop offset="0" stop-color="#ff4b50"/>
          <stop offset="1" stop-color="#b5121a"/>
        </radialGradient>
      </defs>
      <circle cx="80" cy="80" r="78" fill="#5a0a0e" opacity=".7"/>
      <circle cx="80" cy="80" r="60" fill="#2a0306"/>
      <path d="M80 10 A70 70 0 0 1 150 80" fill="none" stroke="var(--alarm-glow)" stroke-width="14" stroke-dasharray="2 2.4"/>
      <circle cx="80" cy="80" r="46" fill="url(#core)"/>
      <text x="80" y="94" text-anchor="middle" font-family="Roboto, sans-serif" font-weight="700" font-size="42" fill="#7a0a10">4</text>
      <text x="80" y="112" text-anchor="middle" font-family="Roboto, sans-serif" font-size="10" fill="#7a0a10">Sec</text>
    </svg>

    <div class="alert">
      <div class="alert__sender">Sekretariat:</div>
      <div class="alert__message">Bitte bleiben Sie<br>wo Sie sind</div>
    </div>

    <nav class="app-nav">
      <svg viewBox="0 0 24 24" aria-label="Einstellungen">
        <path fill="var(--brand-cyan)" fill-rule="evenodd" d="M12 8.5a3.5 3.5 0 1 0 0 7 3.5 3.5 0 0 0 0-7Zm9 5v-3l-2.4-.5a7 7 0 0 0-.7-1.6l1.4-2-2.1-2.1-2 1.4a7 7 0 0 0-1.7-.7L13 2.5h-3l-.5 2.5a7 7 0 0 0-1.6.7l-2-1.4L3.8 6.4l1.4 2a7 7 0 0 0-.7 1.6L2 10.5v3l2.5.5a7 7 0 0 0 .7 1.6l-1.4 2 2.1 2.1 2-1.4a7 7 0 0 0 1.6.7l.5 2.5h3l.5-2.5a7 7 0 0 0 1.7-.7l2 1.4 2.1-2.1-1.4-2a7 7 0 0 0 .7-1.6Z"/>
      </svg>
      <svg viewBox="0 0 24 24" aria-label="Nachrichten">
        <path fill="var(--brand-cyan)" d="M3 3h18v14H8l-5 4Z"/>
        <circle cx="8" cy="10" r="1.4" fill="#0d0607"/>
        <circle cx="12" cy="10" r="1.4" fill="#0d0607"/>
        <circle cx="16" cy="10" r="1.4" fill="#0d0607"/>
      </svg>
    </nav>
  </section>
</main>
</body>
</html>
```